Out of town New Masters of Accounting

size of ad is 7” x 9.6”
please leave one inch on bottom for footer
We want to attract out of town students to join this master's in accounting program.
You DO NOT  have to use a picture of a person.
But if you do, it should be a  male with a white shirt and should not have long hair.(look like a young executive)
THE TEXT OF THE AD IS IN THE ATTACHMENTS
THE CAP LETTERS ARE THE INSTRUCTIONS

The age we are trying to attract is from 20-30 of ages.
- a clear ad .. the text should not take up the entire ad.. it should not be very crowded -
it should be an attractive ad that people would want to see and stand out
- the text very big and take up the entire ad

```html
<!DOCTYPE html>
<html lang="en">
<head>
<meta charset="utf-8">
<title>Remote Masters in Accounting</title>
<link href="https://fonts.googleapis.com/css2?family=Montserrat:wght@400;500;700;800;900&display=swap" rel="stylesheet">
<style>
  :root {
    --blue: #218fdb;
    --ink: #1a1a1a;
    --charcoal: #2f2f2f;
    --grey-light: #c3c5c9;
    --grey-mid: #a9acb1;
    --white: #ffffff;
    --star: #ffe600;
    --footer-dark: #000000;
    --badge-orange: #f4a21d;
  }
  * { margin: 0; padding: 0; box-sizing: border-box; }
  html, body { width: 846px; height: 1200px; overflow: hidden; background: var(--white); }
  body { font-family: "Montserrat", sans-serif; color: var(--ink); }
  .ad { position: relative; width: 846px; height: 1200px; overflow: hidden; }

  /* Hero */
  .hero { position: absolute; left: 0; top: 0; width: 846px; height: 620px;
    background: linear-gradient(100deg, var(--grey-light) 0%, #b9bcc1 55%, #8e9298 100%); }
  .hero-photo { position: absolute; right: 0; top: 0; width: 560px; height: 620px;
    background: radial-gradient(ellipse 46% 52% at 62% 44%, #c99f86 0%, #b58a72 40%, rgba(150,120,105,0.35) 70%, rgba(140,140,145,0) 100%),
                linear-gradient(180deg, rgba(0,0,0,0) 70%, #e9e9ea 100%); }
  .ranking-badge { position: absolute; left: 50px; top: 14px; width: 120px; height: 176px;
    border-radius: 8px; background: var(--badge-orange); opacity: 0.85; }
  .hero-title { position: absolute; left: 46px; top: 228px; font-size: 72px; font-weight: 800;
    color: var(--charcoal); letter-spacing: -1px; line-height: 1; }
  .hero-sub { position: absolute; left: 48px; top: 314px; font-size: 33px; font-weight: 500;
    color: var(--charcoal); line-height: 34px; letter-spacing: 0.5px; }
  .hero-rule { position: absolute; left: 48px; top: 399px; width: 144px; height: 3px; background: var(--charcoal); }
  .date-box { position: absolute; left: 48px; top: 443px; width: 238px; height: 104px; background: var(--blue); }
  .date-box .date { position: absolute; left: 14px; top: 10px; font-size: 34px; font-weight: 900; color: var(--ink); }
  .date-box .divider { position: absolute; left: 0; top: 57px; width: 100%; height: 1px; background: rgba(255,255,255,0.35); }
  .date-box .prices { position: absolute; left: 11px; top: 66px; font-size: 20px; font-weight: 800;
    color: var(--white); text-decoration: underline; text-underline-offset: 3px; }

  /* Blue band */
  .band { position: absolute; left: 0; top: 620px; width: 846px; height: 238px; background: var(--blue); }
  .band .split { position: absolute; left: 425px; top: 0; width: 1px; height: 100%; background: rgba(255,255,255,0.35); }
  .career { position: absolute; left: 76px; top: 44px; }
  .career h2 { font-size: 32px; font-weight: 800; line-height: 31px; color: var(--ink); }
  .career .program { margin-top: 18px; font-size: 24px; font-weight: 600; color: var(--white); line-height: 29px; }
  .career .program u { text-underline-offset: 3px; }
  .rating { position: absolute; left: 475px; top: 50px; width: 340px; }
  .rating h3 { font-size: 26px; font-weight: 800; color: var(--ink); }
  .stars { display: flex; gap: 5px; margin-top: 6px; }
  .rating p { margin-top: 12px; font-size: 16px; font-weight: 500; color: var(--white); line-height: 20px; }
  .rating b { font-weight: 800; }

  /* Placement */
  .placement { position: absolute; left: 76px; top: 898px; }
  .placement h2 { font-size: 24px; font-weight: 800; line-height: 29px; color: var(--ink); }
  .placement ul { list-style: none; margin-top: 20px; margin-left: 31px; }
  .placement li { position: relative; font-size: 21.5px; font-weight: 500; line-height: 26px; }
  .placement li::before { content: ""; position: absolute; left: -17px; top: 10px; width: 8px; height: 8px;
    border-radius: 50%; background: var(--blue); }
  .duration-badge { position: absolute; left: 570px; top: 833px; }

  /* Footer */
  .footer { position: absolute; left: 0; top: 1117px; width: 846px; height: 83px; }
  .footer .call { position: absolute; left: 0; top: 0; width: 425px; height: 83px; background: var(--footer-dark); }
  .call .label { position: absolute; left: 104px; top: 13px; font-size: 14px; font-weight: 500; color: var(--blue); }
  .call .number { position: absolute; left: 103px; top: 25px; font-size: 34px; font-weight: 500; color: var(--white); letter-spacing: 0.5px; }
  .call svg { position: absolute; left: 77px; top: 38px; }
  .footer .contact { position: absolute; left: 425px; top: 0; width: 421px; height: 83px; background: var(--blue);
    color: var(--white); font-size: 12px; font-weight: 500; line-height: 15px; }
  .contact .item { position: absolute; top: 36px; padding-left: 18px; }
  .contact .item svg { position: absolute; left: 0; top: 1px; }
  .contact .address { left: 41px; }
  .contact .web { left: 216px; }
</style>
</head>
<body>
<main class="ad">
  <section class="hero">
    <div class="hero-photo" role="img" aria-label="Portrait of a smiling young man with short hair and glasses in a white T-shirt"></div>
    <div class="ranking-badge" role="img" aria-label="Masters ranking award badge"></div>
    <h1 class="hero-title">All New!</h1>
    <p class="hero-sub">Remote program for<br>out of town students</p>
    <div class="hero-rule"></div>
    <div class="date-box">
      <div class="date">AUGUST 17</div>
      <div class="divider"></div>
      <div class="prices">NEW LOWER PRICES</div>
    </div>
  </section>

  <section class="band">
    <div class="split"></div>
    <div class="career">
      <h2>Advance further<br>in your career</h2>
      <p class="program"><u>Masters of Science</u><br>in Accounting</p>
    </div>
    <div class="rating">
      <h3>Gradvista</h3>
      <div class="stars" aria-label="Five stars">
        <svg width="112" height="20" viewBox="0 0 112 20">
          <g fill="var(--star)">
            <polygon id="s" points="9,1 11.3,7 17.5,7.2 12.6,11 14.3,17 9,13.5 3.7,17 5.4,11 0.5,7.2 6.7,7"/>
            <use href="#s" x="23"/><use href="#s" x="46"/><use href="#s" x="69"/><use href="#s" x="92"/>
          </g>
        </svg>
      </div>
      <p><b>Harrowgate Dunmore University (HDU)</b><br>Master in Accounting Program received<br>the <b>highest possible star rating.</b></p>
    </div>
  </section>

  <section class="placement">
    <h2>PLS/Kestrel Guild<br>Job Placement Advantage</h2>
    <ul>
      <li>96% placement rate</li>
      <li>8 placement coordinators</li>
      <li>Decades of relationships with 100’s of firm</li>
    </ul>
  </section>

  <svg class="duration-badge" width="188" height="188" viewBox="0 0 188 188" aria-label="A masters in only 15 months">
    <defs>
      <filter id="soft" x="-20%" y="-20%" width="140%" height="140%">
        <feDropShadow dx="0" dy="2" stdDeviation="4" flood-opacity="0.18"/>
      </filter>
    </defs>
    <circle cx="94" cy="92" r="91" fill="var(--white)" filter="url(#soft)"/>
    <circle cx="94" cy="92" r="83" fill="var(--blue)"/>
    <path d="M21,92 A73,73 0 0 1 167,92 Z" fill="var(--white)" transform="translate(0,-1)"/>
    <g fill="var(--blue)">
      <polygon points="94,29 96.7,36.5 104.5,36.7 98.3,41.5 100.5,49 94,44.6 87.5,49 89.7,41.5 83.5,36.7 91.3,36.5"/>
      <polygon points="65,43 66.4,47 70.6,47.1 67.3,49.6 68.5,53.6 65,51.3 61.5,53.6 62.7,49.6 59.4,47.1 63.6,47"/>
      <polygon points="123,43 124.4,47 128.6,47.1 125.3,49.6 126.5,53.6 123,51.3 119.5,53.6 120.7,49.6 117.4,47.1 121.6,47"/>
    </g>
    <text x="94" y="78" text-anchor="middle" font-family="Montserrat, sans-serif" font-weight="900" font-size="13" fill="var(--ink)">BRIGHTPATH</text>
    <text x="94" y="109" text-anchor="middle" font-family="Montserrat, sans-serif" font-weight="600" font-size="10.5" fill="var(--ink)">A masters in only</text>
    <text x="94" y="128" text-anchor="middle" font-family="Montserrat, sans-serif" font-weight="900" font-size="15.5" fill="var(--white)">15 months</text>
    <g fill="none" stroke="var(--white)" stroke-width="1.5" stroke-linecap="round">
      <rect x="86" y="142" width="16" height="9" rx="3" transform="rotate(-40 94 146)"/>
      <line x1="98" y1="138" x2="103" y2="134"/>
      <line x1="85" y1="154" x2="89" y2="157"/>
    </g>
  </svg>

  <footer class="footer">
    <div class="call">
      <span class="label">Give us a call</span>
      <svg width="15" height="22" viewBox="0 0 15 22" aria-hidden="true">
        <rect x="1" y="1" width="13" height="20" rx="2" fill="none" stroke="var(--white)" stroke-width="2"/>
        <rect x="3" y="4" width="9" height="11" fill="var(--white)"/>
        <circle cx="7.5" cy="18" r="1.2" fill="var(--white)"/>
      </svg>
      <span class="number">900 555 0142</span>
    </div>
    <div class="contact">
      <div class="item address">
        <svg width="10" height="13" viewBox="0 0 10 13" aria-hidden="true"><path d="M5,0 A5,5 0 0 1 10,5 C10,8 5,13 5,13 C5,13 0,8 0,5 A5,5 0 0 1 5,0 Z" fill="var(--white)"/><circle cx="5" cy="5" r="1.8" fill="var(--blue)"/></svg>
        418 Marlowe St.<br>Edgeford, FL 200410
      </div>
      <div class="item web">
        <svg width="12" height="30" viewBox="0 0 12 30" aria-hidden="true">
          <circle cx="6" cy="6" r="4.5" fill="none" stroke="var(--white)" stroke-width="1.4"/>
          <circle cx="6" cy="6" r="1.6" fill="var(--white)"/>
          <circle cx="6" cy="21" r="5.5" fill="var(--white)"/>
          <path d="M3,18 L6,20 L5,24 M8,17 L9,21" stroke="var(--blue)" stroke-width="1.2" fill="none"/>
        </svg>
        hello@northvale.edu<br>www.northvale.edu
      </div>
    </div>
  </footer>
</main>
</body>
</html>
```